The Get Me Hired as a Game Producer Business Card Design

I am currently looking for a business card to take along with me to the Interactive Makers Summit next year. It's my hope to get a business card that is memorable, fun and professional, and will encourage interest in myself and my abilities.

I'm Australian born and raised, and currently live here. I've studied for several years in Game Development and have managed projects professionally as a producer for around 2-3 years now. My job has been referred to as being a 'fire fighter' (hence the 'Game Dev Fire Dept' comment in the contact information). It's my job to prevent problems before they arise or to solve problems for team members as they happen.

I've got skills in time management, team management, project management, empathy, art and programming, as well as a great sense of humor. Whether or not this is something displayed on the card is your choice.

In past I've used a vector image of my face and colors in brown and blue, but this is not a theme I am particularly attached to if you can come up with something better and more creative.

Target Market(s)

Game Developers, Studio Leads, 25 years old and up

Industry/Entity Type

Business

Contact Information for Business Card

Keloviran,
Corwin Pallish,
corwin@keloviran.com,
Game Producer/Developer (or Game Dev Fire Dept),

Requirements
Nice to have
• Consideration in the design for (or a second design for) a USB drive card.
http://www.drivequill.com.au/products/slim-usb-card

A space for my twitter account: @Keloviran

```html
<!DOCTYPE html>
<html lang="en">
<head>
<meta charset="utf-8">
<title>Keloviran – Corwin Pallish Business Card</title>
<link rel="stylesheet" href="https://fonts.googleapis.com/css2?family=Open+Sans:wght@300;400&display=swap">
<style>
  :root {
    --paper: #ffffff;
    --ink-light: #f2f6f6;
    --teal-glow: #cfe3e2;
    --teal-mid: #2f7c7a;
    --teal-deep: #0f3a3b;
    --night: #060c0d;
    --connector: #2b2b2b;
    --contact-gold: #d4c27c;
  }
  * { margin: 0; padding: 0; box-sizing: border-box; }
  html, body {
    width: 1200px;
    height: 676px;
    overflow: hidden;
    background: var(--paper);
  }
  .card {
    position: relative;
    width: 1200px;
    height: 676px;
    background: var(--paper);
    overflow: hidden;
    font-family: "Open Sans", Arial, sans-serif;
  }
  .card__artwork {
    position: absolute;
    left: 152px;
    top: 0;
    width: 1048px;
    height: 676px;
    background:
      radial-gradient(ellipse 380px 300px at 490px 205px, var(--teal-glow) 0%, rgba(120,170,170,0.55) 25%, rgba(47,124,122,0.35) 55%, rgba(15,58,59,0) 100%),
      linear-gradient(180deg, #3f5f60 0%, var(--teal-deep) 45%, #0b2426 75%, var(--night) 100%);
  }
  .usb-connector {
    position: absolute;
    left: 0;
    top: 296px;
    width: 342px;
    height: 138px;
  }
  .card__details {
    position: absolute;
    left: 152px;
    right: 0;
    top: 346px;
    text-align: center;
    color: var(--ink-light);
  }
  .details__company {
    font-weight: 300;
    font-size: 58px;
    line-height: 72px;
    letter-spacing: 1px;
  }
  .details__line {
    font-weight: 300;
    font-size: 33px;
    line-height: 47px;
    letter-spacing: 1px;
  }
  .details__company, .details__line { margin-left: 0; }
</style>
</head>
<body>
  <div class="card">
    <div class="card__artwork" role="img" aria-label="Abstract teal light-burst background with soft curved streaks and bokeh"></div>

    <svg class="usb-connector" viewBox="0 0 342 138" aria-hidden="true">
      <rect x="0" y="0" width="342" height="138" fill="var(--connector)"/>
      <rect x="12" y="12" width="134" height="114" fill="var(--paper)"/>
      <rect x="18" y="23" width="90" height="15" fill="var(--contact-gold)"/>
      <rect x="18" y="47" width="82" height="14" fill="var(--contact-gold)"/>
      <rect x="18" y="71" width="82" height="14" fill="var(--contact-gold)"/>
      <rect x="18" y="95" width="90" height="15" fill="var(--contact-gold)"/>
      <rect x="230" y="0" width="112" height="138" fill="var(--paper)"/>
    </svg>

    <div class="card__details">
      <p class="details__company">Keloviran</p>
      <p class="details__line">Corwin Pallish</p>
      <p class="details__line">Game Producer/Developer</p>
      <p class="details__line">corwin@keloviran.com</p>
      <p class="details__line">@Keloviran</p>
    </div>
  </div>
</body>
</html>
```